Stationery Design Project for Holloway Kenbukan Karate Studio

We Need a Stationery Design for a Karate School Teaching Okinawa Shorin Ryu Karate in Fernmoor Bay, Westmarch, U.S.A.

Target Market(s)

Adults Base Western Speaking aged between 25 and 65 yrs, old that handle household budgets

Industry/Entity Type

School

Requirements
Must have
• Name of business: Holloway Kenbukan Karate Studio
Address: Larkspur Commons 18342 US Hwy. 91
Fernmoor Bay, Westmarch. 33914
Phone # : 407-555-0183
email : Hollowaykenbukanstudio@mailgrove.example
Logo - attatched

```html
<!DOCTYPE html>
<html lang="en">
<head>
<meta charset="utf-8">
<title>Holloway Kenbukan Karate Studio – Letterhead</title>
<link rel="stylesheet" href="https://fonts.googleapis.com/css2?family=Arimo:wght@400;700&family=Pinyon+Script&family=Open+Sans:wght@400&display=swap">
<style>
  :root {
    --paper: #ffffff;
    --ink: #333333;
    --ink-strong: #111111;
    --accent: #d0202a;
    --decor: #eeeeee;
  }
  * { margin: 0; padding: 0; box-sizing: border-box; }
  html, body { width: 870px; height: 1200px; overflow: hidden; background: var(--paper); }
  .letterhead {
    position: relative;
    width: 870px;
    height: 1200px;
    overflow: hidden;
    background: var(--paper);
    font-family: "Arimo", Arial, sans-serif;
    color: var(--ink);
  }
  .backdrop-mark {
    position: absolute;
    right: -150px;
    bottom: -170px;
    width: 520px;
    height: 520px;
    border-radius: 50%;
    background: var(--decor);
  }
  .brand {
    position: absolute;
    top: 36px;
    right: 46px;
    width: 130px;
    display: flex;
    flex-direction: column;
    align-items: center;
    gap: 12px;
  }
  .brand-dot {
    width: 54px;
    height: 54px;
    border-radius: 50%;
    background: var(--accent);
  }
  .brand-name {
    font-weight: 700;
    font-size: 17px;
    line-height: 1.15;
    text-align: center;
    color: var(--ink-strong);
    text-transform: uppercase;
  }
  .salutation {
    position: absolute;
    top: 230px;
    left: 77px;
    font-size: 20.5px;
    color: var(--ink);
  }
  .letter-body {
    position: absolute;
    top: 284px;
    left: 85px;
    width: 740px;
    font-size: 20.8px;
    line-height: 25px;
    color: var(--ink);
  }
  .letter-body p + p { margin-top: 25px; }
  .signature-name {
    position: absolute;
    top: 868px;
    left: 52px;
    font-family: "Pinyon Script", cursive;
    font-size: 56px;
    line-height: 1;
    color: var(--ink-strong);
  }
  .signature-role {
    position: absolute;
    top: 932px;
    left: 89px;
    font-size: 19px;
    color: var(--ink);
  }
  .contact {
    position: absolute;
    top: 1076px;
    left: 24px;
    font-family: "Open Sans", Arial, sans-serif;
    font-size: 14px;
    line-height: 20.4px;
    color: var(--ink-strong);
  }
  .contact-label { color: var(--accent); font-size: 15px; margin-right: 3px; }
</style>
</head>
<body>
<main class="letterhead">
  <div class="backdrop-mark" aria-hidden="true"></div>

  <header class="brand">
    <span class="brand-dot" aria-hidden="true"></span>
    <span class="brand-name">Holloway Kenbukan<br>Karate Studio</span>
  </header>

  <p class="salutation">Dear Sir / Madam,</p>

  <section class="letter-body">
    <p>Lorem ipsum dolor sit amet, consectetur adipisicing elit, sed do eiusmod<br>tempor incididunt ut labore et dolore magna aliqua. Ut enim ad minim<br>veniam, quis nostrud exercitation ullamco laboris nisi ut aliquip ex ea com-<br>modo consequa.Lorem ipsum dolor sit amet, consectetur adipisicing elit,<br>ed do eiusmod tempor incididunt ut labore et dolore magna aliqua. Ut enim<br>ad minim veniam, quis.</p>
    <p>Lorem ipsum dolor sit amet, consectetur adipisicing elit, sed do eiusmod<br>tempor incididunt ut labore et dolore magna aliqua. Ut enim ad minim<br>veniam, quis nostrud exercitation ullamco laboris nisi ut aliquip ex ea com-<br>modo consequa.Lorem ipsum dolor sit amet, consectetur adipisicing elit,<br>ed do eiusmod tempor incididunt ut labore et dolore magna aliqua. Ut enim<br>ad minim veniam, quis.</p>
    <p>Lorem ipsum dolor sit amet, consectetur adipisicing elit, sed do eiusmod<br>tempor incididunt ut labore et dolore magna aliqua. Ut enim ad minim<br>veniam, quis nostrud exercitation ullamco laboris nisi ut aliquip ex ea com-<br>modo consequa.Lorem ipsum dolor sit amet, consectetur adipisicing elit,<br>ed do eiusmod tempor incididunt ut labore et dolore magna aliqua. Ut enim<br>ad minim veniam, quis.</p>
  </section>

  <p class="signature-name">Your name</p>
  <p class="signature-role">Designation</p>

  <footer class="contact">
    <p>Larkspur Commons</p>
    <p>18342 US Hwy. 91</p>
    <p>Fernmoor Bay, Westmarch. 33914</p>
    <p><span class="contact-label">t:</span>407-555-0183</p>
    <p><span class="contact-label">e:</span>Hollowaykenbukanstudio@mailgrove.example</p>
  </footer>
</main>
</body>
</html>
```